Professional and creative business card design for recruiting service providers

Our company supports German medium-sized companies in filling vacancies promptly. For this we use social media marketing and bring our customers into the visibility.

We want a professional but also creative design for our business cards.

Please look at halvenrick-consult.de to get an impression of our CI.

Target Market(s)

Small and medium-sized companies in Germany from the industry

Industry/Entity Type

Industrie, Handwerk

Contact Information for Business Card

Name, Position, Telefonnummer, Email, Website

Colors
EE7325
F08F49
F5BC92
FAE3D3
FDF4ED

Requirements
Must have
• A picture of the employee and in the style of www.halvenrick-consult.de

```html
<!DOCTYPE html>
<html lang="de">
<head>
<meta charset="utf-8">
<title>Halvenrick Consult – Visitenkarte</title>
<link href="https://fonts.googleapis.com/css2?family=Montserrat:wght@400;600;700;800&display=swap" rel="stylesheet">
<style>
  :root{
    --orange:#EE7325;
    --orange-soft:#F08F49;
    --ink:#1f1f21;
    --card-white:#ffffff;
    --card-black:#1b1b1d;
    --backdrop:#e9e7e5;
    --text-grey:#2e2e30;
  }
  *{box-sizing:border-box;margin:0;padding:0}
  html,body{width:1200px;height:948px;overflow:hidden}
  body{
    background:var(--backdrop);
    font-family:"Montserrat",sans-serif;
    display:flex;flex-direction:column;align-items:center;justify-content:center;gap:24px;
  }
  .card{
    width:760px;height:430px;border-radius:28px;position:relative;overflow:hidden;
    box-shadow:0 10px 30px rgba(0,0,0,.18);
  }
  /* back side */
  .card--back{background:var(--card-black)}
  .card--back .pattern{
    position:absolute;inset:0;
    background:linear-gradient(135deg,#232325 0%,#161618 100%);
  }
  .card--back .corner-mark{
    position:absolute;right:48px;top:44px;
    width:22px;height:22px;background:var(--orange);border-radius:4px;
  }
  /* front side */
  .card--front{background:var(--card-white)}
  .brand{
    position:absolute;left:52px;top:58px;display:flex;align-items:center;gap:16px;
  }
  .brand__square{width:46px;height:46px;background:var(--orange)}
  .brand__name{
    font-weight:700;font-size:25px;line-height:1.05;letter-spacing:2px;color:var(--ink);
    text-transform:uppercase;
  }
  .accent-bar{
    position:absolute;left:0;top:236px;width:30px;height:44px;background:var(--orange);
  }
  .person{position:absolute;left:52px;top:222px}
  .person__name{
    font-weight:800;font-size:30px;letter-spacing:1px;color:var(--orange);text-transform:uppercase;
  }
  .person__role{font-weight:700;font-size:17px;color:var(--text-grey);margin-top:2px}
  .contacts{position:absolute;left:52px;top:300px;list-style:none}
  .contacts li{
    display:flex;align-items:center;gap:10px;font-size:17px;font-weight:400;color:var(--text-grey);
    margin-bottom:8px;letter-spacing:.3px;
  }
  .contacts svg{width:16px;height:16px;flex:none}
  .photo{
    position:absolute;right:0;top:0;width:340px;height:100%;
    background:linear-gradient(180deg,#ffffff 0%,#f1ece8 22%,#3a3a40 55%,#1c1c20 100%);
  }
</style>
</head>
<body>

  <section class="card card--back" aria-label="Kartenrückseite">
    <div class="pattern" role="img" aria-label="Dunkles geprägtes Muster aus geometrischen Formen"></div>
    <div class="corner-mark"></div>
  </section>

  <section class="card card--front" aria-label="Kartenvorderseite">
    <div class="brand">
      <div class="brand__square"></div>
      <div class="brand__name">Halvenrick<br>Consult</div>
    </div>

    <div class="accent-bar"></div>
    <div class="person">
      <div class="person__name">Jonas Halvenrick</div>
      <div class="person__role">Gründer</div>
    </div>

    <ul class="contacts">
      <li>
        <svg viewBox="0 0 16 16"><path fill="var(--orange)" d="M3.2 1.5l2.3 2.6-1.3 1.6c.9 2 2.2 3.3 4.2 4.2l1.6-1.3 2.6 2.3-1.4 2.4C6.2 13 3 9.8 1.1 4.8z"/></svg>
        (123) 456 7890
      </li>
      <li>
        <svg viewBox="0 0 16 16"><rect x="1" y="3" width="14" height="10" rx="1" fill="var(--orange)"/><path d="M1.5 3.8L8 9l6.5-5.2" fill="none" stroke="#fff" stroke-width="1.4"/></svg>
        info@halvenrick-consult.de
      </li>
      <li>
        <svg viewBox="0 0 16 16"><g fill="none" stroke="var(--orange)" stroke-width="1.4"><circle cx="8" cy="8" r="6.5"/><ellipse cx="8" cy="8" rx="3" ry="6.5"/><path d="M1.5 8h13M3 4.5h10M3 11.5h10"/></g></svg>
        www.halvenrick-consult.de
      </li>
    </ul>

    <div class="photo" role="img" aria-label="Porträtfoto des Gründers in dunklem Sakko und Rollkragenpullover vor weißem Hintergrund"></div>
  </section>

</body>
</html>
```